Painting Valtoni Renovations New buildings

Paint jobs plasterwork renovations new building customer painter paper drywall Entsorgungen.neukunden win color splash pleasure in colors competent clean fast reliable new try build demolition color combinations color concepts offers washing façade painting wood stains new projects old building renovations yes no beautiful new old sell secure solve paint over paint paint spray paint lye assemble disassemble sell buy trade oil dust new old assembly disassembly putty sanding fashion devastation copying belief feng shui kleopatra pompes beer colors swamp lime abrasion release tighten

Target Market(s)

construction industry

Contact Information for Business Card

Maler

Font styles to use
Serif

Colors
f04a50
959595

Requirements
Must have
• elegant appearance
Nice to have
• simply goal-oriented clientele in detail
Should not have
• too colorful

```html
<!DOCTYPE html>
<html lang="de">
<head>
<meta charset="utf-8">
<title>Ardena Malerbetrieb – Visitenkarte</title>
<link href="https://fonts.googleapis.com/css2?family=Lora:wght@400;600&display=swap" rel="stylesheet">
<style>
  :root {
    --page: #e9e9e9;
    --card: #ffffff;
    --accent: #f04a50;
    --accent-deep: #d8393f;
    --grey: #959595;
    --ink: #4f4f4f;
    --rule: #d4d4d4;
    --white: #ffffff;
  }
  * { box-sizing: border-box; margin: 0; padding: 0; }
  html, body { width: 1200px; height: 1200px; overflow: hidden; }
  body {
    background: var(--page);
    font-family: "Lora", Georgia, serif;
    position: relative;
  }
  .card {
    position: absolute;
    left: 257px;
    width: 686px;
    height: 392px;
    box-shadow: 0 18px 26px rgba(0,0,0,0.18);
  }
  .card-front { top: 165px; background: var(--card); }
  .card-back {
    top: 653px;
    background: linear-gradient(180deg, var(--accent), var(--accent-deep));
  }
  .front-band {
    position: absolute; left: 0; right: 0; bottom: 0;
    height: 15px; background: var(--accent);
  }
  .brand {
    position: absolute;
    left: 40px; width: 340px; top: 158px;
    display: flex; align-items: center; justify-content: center; gap: 14px;
  }
  .brand-swatch {
    width: 20px; height: 20px;
    background: var(--accent);
  }
  .brand-name {
    font-size: 62px; font-weight: 600; color: var(--grey);
    letter-spacing: 0.5px; line-height: 1;
  }
  .divider {
    position: absolute; left: 389px; top: 79px;
    width: 2px; height: 240px; background: var(--rule);
  }
  .contact { position: absolute; left: 417px; top: 82px; }
  .person-name {
    font-size: 26px; font-weight: 600; color: var(--accent); line-height: 1.15;
  }
  .person-role {
    font-size: 18px; color: var(--grey); line-height: 1.15;
  }
  .address {
    margin-top: 14px; font-size: 16px; color: var(--ink);
    line-height: 21px;
  }
  .contact-list { list-style: none; margin-top: 12px; }
  .contact-list li {
    display: flex; align-items: center; gap: 10px;
    font-size: 16px; color: var(--ink); height: 22px;
  }
  .contact-list svg { width: 15px; height: 15px; fill: var(--accent); flex: none; }
  .back-brand {
    position: absolute; left: 0; right: 0; top: 140px;
    display: flex; align-items: center; justify-content: center; gap: 14px;
  }
  .back-brand .brand-swatch { background: var(--white); }
  .back-brand .brand-name { color: var(--white); }
  .back-url {
    position: absolute; left: 0; right: 0; top: 336px;
    text-align: center; color: var(--white);
    font-size: 17px; letter-spacing: 12px; padding-left: 12px;
  }
</style>
</head>
<body>
  <section class="card card-front">
    <div class="brand">
      <span class="brand-swatch"></span>
      <span class="brand-name">Ardena</span>
    </div>
    <div class="divider"></div>
    <div class="contact">
      <p class="person-name">Merenda Valtoni</p>
      <p class="person-role">President</p>
      <p class="address">4120 Linden Court<br>Fairbanks, Alaska 34120</p>
      <ul class="contact-list">
        <li><svg viewBox="0 0 16 16"><path d="M3 1l3 3-1.5 2c1 2 2.5 3.5 4.5 4.5L11 9l3 3-2 2C6 13 2 9 1 3z"/></svg>555-214-3086</li>
        <li><svg viewBox="0 0 16 16"><path d="M4 0h8v16H4zM5.5 2v10h5V2zM7 13.5h2V15H7z" fill-rule="evenodd"/></svg>555-617-4422</li>
        <li><svg viewBox="0 0 16 16"><path d="M4 1h8v5H4zM1 7h14v6h-3v2H4v-2H1zM5 11v3h6v-3z" fill-rule="evenodd"/></svg>555-390-7751</li>
        <li><svg viewBox="0 0 16 16"><path d="M1 3h14v10H1zM2.5 4.5L8 9l5.5-4.5v7h-11z" fill-rule="evenodd"/></svg>info@ardena.com</li>
        <li><svg viewBox="0 0 16 16"><circle cx="8" cy="8" r="7"/><path d="M5 4c2 0 3 1 2 3s-3 1-3 3 2 1 2 3" stroke="#fff" stroke-width="1.3" fill="none"/></svg>www.ardena.com</li>
      </ul>
    </div>
    <div class="front-band"></div>
  </section>

  <section class="card card-back">
    <div class="back-brand">
      <span class="brand-swatch"></span>
      <span class="brand-name">Ardena</span>
    </div>
    <p class="back-url">www.ardena.com</p>
  </section>
</body>
</html>
```